Digital Billboard Design: Winter Sales Event

I own a boutique furniture store in Calgary, AB (maplecrestdecor.ca) and I am looking to advertise our winter sale event on a new curved digital billboard (specs attached including required file type).

I have this billboard rented for 52-weeks so I will be looking to change the design every 4-weeks (i.e. this is intended to be an ongoing project).

The objective of this first billboard is to raise awareness around our annual winter sales event. The store itself is only a few blocks from the billboard so those commuting into downtown are just a short drive from the store.

I am looking for a fresh, clean, contemporary look that will grab your attention as you drive into downtown Calgary without presenting to much info so as to be distracting (and overwhelming -- the billboard does not need to contain all info on my current marketing material). I should also note that the store caters to a higher-end, more sophisticated clientele so the graphics need to reflect the brand (i.e. we are not Brennick Furniture or Couch Depot!).

I have attached three files:

Billboard specs
Current marketing material advertising sale (and all relevant data)
An idea that is from an American furniture store that I think is interesting

Target Market(s)

Upper middle class, sophisticated client who appreciates the finer things in life.

Industry/Entity Type

Furniture Store

Font styles to use
Sans Serif

Requirements
Must have
• Company Logo
• Winter Sales Event - 20 to 60% off
• Address: 2743 8th Ave SW
Nice to have
• Image of furniture -- see our website www.maplecrestdecor.ca -- any photo from this site can be used
Should not have
• Too much text or visual distration

```html
<!DOCTYPE html>
<html lang="en">
<head>
<meta charset="utf-8">
<title>Maplecrest Decor – Winter Sales Event</title>
<link rel="stylesheet" href="https://fonts.googleapis.com/css2?family=Oxanium:wght@400;500&display=swap">
<style>
  :root {
    --page: #ffffff;
    --plum: #976496;
    --ink: #3f3f42;
    --ink-soft: #2e2e30;
    --photo-light: #f1f1ef;
    --photo-mid: #c9c9c6;
    --photo-dark: #8e8e90;
  }
  * { margin: 0; padding: 0; box-sizing: border-box; }
  html, body {
    width: 1200px;
    height: 1001px;
    overflow: hidden;
    background: var(--page);
  }
  .canvas {
    position: relative;
    width: 1200px;
    height: 1001px;
    background: var(--page);
    font-family: "Oxanium", "Eurostile", sans-serif;
  }
  .billboard {
    position: absolute;
    left: 156px;
    top: 288px;
    width: 901px;
    height: 433px;
  }
  .furniture-photo {
    position: absolute;
    left: 0;
    top: 0;
    width: 439px;
    height: 288px;
    background: linear-gradient(180deg, var(--photo-light) 0%, var(--photo-light) 60%, var(--photo-mid) 78%, var(--photo-dark) 100%);
  }
  .photo-grid {
    position: absolute;
    left: 0;
    top: 0;
  }
  .sale-panel {
    position: absolute;
    left: 439px;
    top: 0;
    width: 462px;
    height: 288px;
    background: var(--plum);
    color: var(--page);
    overflow: hidden;
  }
  .sale-title {
    position: absolute;
    left: 19px;
    top: 183px;
    font-size: 38px;
    font-weight: 400;
    letter-spacing: 2.5px;
    line-height: 1;
    white-space: nowrap;
  }
  .sale-discount {
    position: absolute;
    left: 19px;
    top: 233px;
    font-size: 30px;
    font-weight: 400;
    letter-spacing: 7.5px;
    line-height: 1;
    white-space: nowrap;
  }
  .store-box {
    position: absolute;
    left: 0;
    top: 288px;
    width: 901px;
    height: 145px;
    border: 2px solid var(--plum);
    background: var(--page);
    text-align: center;
  }
  .store-name {
    position: absolute;
    left: 0;
    right: 0;
    top: 22px;
    font-size: 45px;
    font-weight: 500;
    letter-spacing: 1.5px;
    color: var(--ink);
    line-height: 1;
    white-space: nowrap;
  }
  .store-address {
    position: absolute;
    left: 0;
    right: 0;
    top: 82px;
    font-size: 29px;
    font-weight: 400;
    letter-spacing: 8px;
    color: var(--ink-soft);
    line-height: 1;
    white-space: nowrap;
  }
</style>
</head>
<body>
<main class="canvas">
  <section class="billboard">
    <div class="furniture-photo" role="img" aria-label="Photo of a grey sideboard with a crystal table lamp, a framed mirror and a black dining chair against a white wall"></div>
    <svg class="photo-grid" width="440" height="289" viewBox="0 0 440 289" aria-hidden="true">
      <rect x="1" y="1" width="438" height="288" fill="none" stroke="var(--plum)" stroke-width="2"/>
      <line x1="146" y1="0" x2="146" y2="289" stroke="var(--plum)" stroke-width="2.5"/>
      <line x1="294" y1="0" x2="294" y2="289" stroke="var(--plum)" stroke-width="2.5"/>
      <line x1="0" y1="144" x2="440" y2="144" stroke="var(--plum)" stroke-width="2.5"/>
    </svg>
    <div class="sale-panel">
      <h1 class="sale-title">WINTER SALES EVENT</h1>
      <p class="sale-discount">20 TO 60% OFF</p>
    </div>
    <div class="store-box">
      <h2 class="store-name">MAPLECREST DECOR</h2>
      <p class="store-address">2743 8TH AVE SW, CALGARY, AB.</p>
    </div>
  </section>
</main>
</body>
</html>
```